Business Card Design - front and back

Residential real estate agent looking for a an emphasis on my first name (last name is hard to spell).  Would love the slogan "It's more than a contract" on the card.  Simple, easy to read business card that makes people want to pick it up and remember it.  The Bright Lantern Realty has to be on the front of card but does not need to be the emphasis.  Prefer locations on the back.  Would love a home on it.  Looking for simply elegant in the card that shows I am a non-complicated, warm, honest real estate agent.
NEED ONE OF MY PICTURES ON THE CARD.  LEAVING WHICH ONE UP TO THE DESIGNER.

Industry/Entity Type
Real Estate
Contact Information for Business Card
Gloria Penwick, Broker Associate, Bright Lantern Realty, 727-481-6054 cell, hereisgloria@maplenest.example, listedbygloria.example, Bright Lantern Realty locations: 48217 Orrington Blvd Ste 101, Tampa, FL  30918, 2948 Velo Ct Ste 101, New Port Richey, FL  30742
I NEED THIS DOUBLE SIDED - THE SELECTION BELOW WILL NOT ALLOW IT?
Requirements
Must have
- Emphasis on my first name
a home in it
LOVE Marla dobrin's logo which sits on the left side in the margin at
http://marladobrin.quillagentsite.example/
Something with that idea is exactly what I am looking for.
Nice to have
- Nice script that is readable.
Should not have
- I am looking for something simple

```html
<!DOCTYPE html>
<html lang="en">
<head>
<meta charset="utf-8">
<title>Gloria Penwick – Business Card</title>
<link rel="stylesheet" href="https://fonts.googleapis.com/css2?family=Arimo:ital,wght@0,400;0,700;1,400&display=swap">
<style>
  :root {
    --backdrop: #6f7173;
    --teal: #1aa394;
    --teal-deep: #0f8a7d;
    --silver-light: #f2f2f2;
    --silver: #c9c9cb;
    --silver-dark: #9c9c9f;
    --ink: #111111;
    --paper: #f4f4f4;
    --white: #ffffff;
  }
  * { box-sizing: border-box; margin: 0; padding: 0; }
  html, body {
    width: 1200px; height: 900px; overflow: hidden;
    background: var(--backdrop);
    font-family: "Arimo", Arial, sans-serif;
  }
  .sheet {
    position: relative; width: 1200px; height: 900px;
  }
  .card {
    position: absolute; top: 155px;
    width: 340px; height: 590px;
    overflow: hidden;
    box-shadow: 0 14px 30px rgba(0,0,0,0.35);
  }
  .card--front { left: 220px; background: radial-gradient(ellipse at 50% 38%, var(--silver-light) 0%, var(--silver) 55%, var(--silver-dark) 100%); }
  .card--back { left: 640px; background: var(--teal); }

  /* front */
  .front-band { position: absolute; inset: 0; width: 100%; height: 100%; }
  .agency { position: absolute; top: 88px; width: 100%; text-align: center; }
  .agency__name { font-size: 18px; color: var(--ink); }
  .agency__slogan { font-size: 15px; font-style: italic; color: var(--ink); margin-top: 3px; }
  .home-art {
    position: absolute; left: 95px; top: 185px; width: 160px; height: 205px;
    background: linear-gradient(180deg, var(--teal) 0%, var(--teal-deep) 100%);
    border-top: 4px solid var(--ink);
  }
  .agent-name { position: absolute; top: 385px; left: 0; width: 100%; text-align: center; }
  .agent-name__first { font-size: 58px; line-height: 1; color: var(--ink); letter-spacing: -1px; }
  .agent-name__last { font-size: 22px; color: var(--white); margin-top: 0; padding-left: 50px; }
  .agent-name__title { font-size: 13px; color: var(--white); letter-spacing: 5px; margin-top: 2px; padding-left: 30px; }

  /* back */
  .back-curve { position: absolute; top: 0; left: 0; width: 340px; height: 300px; }
  .portrait {
    position: absolute; left: 80px; top: 18px; width: 180px; height: 180px; border-radius: 50%;
    background: radial-gradient(circle at 50% 40%, #d8a27f 0%, #a0613a 55%, #4a3a33 100%);
    border: 5px solid var(--silver-light);
    box-shadow: 0 3px 8px rgba(0,0,0,0.35);
  }
  .phone {
    position: absolute; top: 212px; width: 100%; text-align: center;
    font-size: 30px; color: var(--ink); display: flex; justify-content: center; align-items: center; gap: 6px;
  }
  .phone svg { width: 20px; height: 20px; }
  .contact { position: absolute; top: 300px; left: 36px; right: 20px; font-size: 15px; color: var(--ink); line-height: 1.2; }
  .locations {
    position: absolute; bottom: 0; left: 0; width: 100%; height: 95px;
    background: var(--paper);
  }
  .locations__band { position: absolute; top: 0; left: 0; right: 0; height: 60px; background: var(--teal); }
  .locations__list { position: absolute; top: 12px; left: 26px; font-size: 10px; color: var(--ink); line-height: 1.55; }
</style>
</head>
<body>
<main class="sheet">

  <section class="card card--front" aria-label="Card front">
    <svg class="front-band" viewBox="0 0 340 590" aria-hidden="true">
      <path d="M0 410 L95 392 L255 392 L340 400 V590 H0 Z" fill="var(--teal)"/>
      <rect x="0" y="545" width="340" height="45" fill="var(--paper)"/>
    </svg>
    <header class="agency">
      <p class="agency__name">The Bright Lantern Realty</p>
      <p class="agency__slogan">"It's more than a contract"</p>
    </header>
    <div class="home-art" role="img" aria-label="Illustration of teal home rooftops"></div>
    <div class="agent-name">
      <p class="agent-name__first">Gloria</p>
      <p class="agent-name__last">Penwick</p>
      <p class="agent-name__title">Broker Associate</p>
    </div>
  </section>

  <section class="card card--back" aria-label="Card back">
    <svg class="back-curve" viewBox="0 0 340 300" aria-hidden="true">
      <defs>
        <radialGradient id="silverGlow" cx="50%" cy="30%" r="70%">
          <stop offset="0" stop-color="var(--silver-light)"/>
          <stop offset="0.6" stop-color="var(--silver)"/>
          <stop offset="1" stop-color="var(--silver-dark)"/>
        </radialGradient>
      </defs>
      <path d="M0 0 H340 V185 C300 190 285 272 170 274 C55 272 40 190 0 185 Z" fill="url(#silverGlow)"/>
    </svg>
    <div class="portrait" role="img" aria-label="Portrait photograph of Gloria Penwick"></div>
    <p class="phone">
      <svg viewBox="0 0 24 24" aria-hidden="true"><circle cx="12" cy="12" r="10.5" fill="none" stroke="var(--ink)" stroke-width="1.5"/><path d="M8.5 6.5l2 2.5-1.2 1.4c.7 1.6 1.9 2.8 3.4 3.5l1.4-1.2 2.5 2-1.2 1.8c-3.8-.4-7.4-4-7.8-7.8z" fill="var(--ink)"/></svg>
      727-481-6054
    </p>
    <div class="contact">
      <p>email:hereisgloria@maplenest.example</p>
      <p>www.listedbygloria.example</p>
    </div>
    <div class="locations">
      <div class="locations__band"></div>
      <div class="locations__list">
        <p>48217 Orrington Blvd Ste 101, Tampa, FL 30918</p>
        <p>2948 Velo Ct Ste 101, New Port Richey, FL 30742</p>
      </div>
    </div>
  </section>

</main>
</body>
</html>
```